Holbys Pet Care

Hi. I need a business card /logo for my pet care business. Im thinking about a dogs paw print. Although i do look after other pets so don't want to restrict my self. Open to suggestions on colour etc but like greens and purples.The name of my business is holby's pet care. The logo could be just an image or have holbys power care on it. An option to do either would be great. For the winner i also would like a Web page (word press template if possible) designed if you can, of course I'll pay additional for this. Look forward to your ideas!

```html
<!DOCTYPE html>
<html lang="en">
<head>
<meta charset="UTF-8">
<title>Holby's Pet Care – Business Card</title>
<link href="https://fonts.googleapis.com/css2?family=Open+Sans:wght@400;600;700&display=swap" rel="stylesheet">
<style>
  :root {
    --backdrop: #c9d3db;
    --card-top: #e6ecf0;
    --card-top-edge: #d6dee4;
    --teal: #1aa58c;
    --teal-text: #1fb597;
    --charcoal: #1f2224;
    --charcoal-light: #2c3033;
    --ink: #3a3d40;
    --white: #ffffff;
  }
  * { margin: 0; padding: 0; box-sizing: border-box; }
  html, body {
    width: 1200px;
    height: 1084px;
    overflow: hidden;
    background: var(--backdrop);
    font-family: "Open Sans", Arial, sans-serif;
  }
  .canvas {
    position: relative;
    width: 1200px;
    height: 1084px;
  }
  .business-card {
    position: absolute;
    left: 80px;
    top: 222px;
    width: 1040px;
    height: 640px;
    border-radius: 30px;
    overflow: hidden;
    box-shadow: 0 10px 30px rgba(40, 55, 70, 0.18);
    display: flex;
    flex-direction: column;
  }
  .card-brand {
    height: 350px;
    background: linear-gradient(180deg, var(--card-top) 0%, var(--card-top-edge) 100%);
    display: flex;
    flex-direction: column;
    align-items: center;
    justify-content: flex-end;
    padding-bottom: 36px;
  }
  .brand-mark {
    display: flex;
    align-items: center;
    gap: 22px;
  }
  .brand-dot {
    width: 56px;
    height: 56px;
    border-radius: 50%;
    background: var(--teal);
  }
  .brand-name {
    font-weight: 600;
    font-size: 62px;
    color: var(--teal);
    letter-spacing: 1px;
  }
  .services-band {
    height: 28px;
    background: var(--teal);
    color: var(--charcoal);
    font-size: 19px;
    letter-spacing: 3px;
    text-align: center;
    line-height: 28px;
    white-space: nowrap;
  }
  .card-contact {
    flex: 1;
    background:
      radial-gradient(circle, rgba(255,255,255,0.05) 1px, transparent 1.5px) 0 0 / 8px 8px,
      linear-gradient(180deg, var(--charcoal-light) 0%, var(--charcoal) 100%);
    display: flex;
    flex-direction: column;
    align-items: center;
    padding-top: 50px;
    gap: 6px;
  }
  .contact-phone {
    font-weight: 700;
    font-size: 42px;
    color: var(--teal-text);
    letter-spacing: 1px;
  }
  .contact-line {
    font-weight: 600;
    font-size: 32px;
    color: var(--white);
  }
</style>
</head>
<body>
  <main class="canvas">
    <article class="business-card">
      <header class="card-brand">
        <div class="brand-mark">
          <span class="brand-dot"></span>
          <span class="brand-name">Holby's Pet Care</span>
        </div>
      </header>
      <div class="services-band">dog walking. Pet boarding. Home visits for feeding etc.</div>
      <section class="card-contact">
        <p class="contact-phone">919.555.0172</p>
        <p class="contact-line">Holby@holbyspetcare.co.uk</p>
        <p class="contact-line">www.holbyspetcare.co.uk/community</p>
      </section>
    </article>
  </main>
</body>
</html>
```